Construction machinery rental / heavy equipment rental needs a nice billboard

We need a billboard for our company.
We rent out construction machinery such as excavators, wheel loaders, wheel dumpers and so on...

I would like an elegant, simple, dark design.
Colors: black yellow grey white

The following must be on the billboard:
Logo
phone number: 078 / 513 90 41
website: www.kiesgrube-talwerk.ch
the machines I rent out: Bagger bis 10T, Radlader, Dumper, Raupenkipper

the font in the logo is: Square 721

Final format 2950 x 1900mm
I have uploaded pictures:
"Excavator 1-6" are my pictures, which can be used
"Sample 1-4" are pictures whose style I like
"Billboard" are billboards which I like

Requirements
Must have
• The following must be on the billboard: Logo phone number: 078 / 513 90 41 website: www.kiesgrube-talwerk.ch the machines I rent out: Bagger bis 10T, Radlader, Dumper, Raupenkipper

```html
<!DOCTYPE html>
<html lang="de">
<head>
<meta charset="utf-8">
<title>Talwerk Baumaschinenvermietung – Billboard</title>
<link rel="stylesheet" href="https://fonts.googleapis.com/css2?family=Exo+2:ital,wght@0,700;0,800;1,800;1,900&display=swap">
<style>
  :root {
    --page: #f2f2f2;
    --black: #050505;
    --plate: #141414;
    --gold-light: #f3d98a;
    --gold: #d6ad3c;
    --gold-dark: #8f6a17;
    --white: #ffffff;
    --grey: #8a8a8a;
  }
  * { margin: 0; padding: 0; box-sizing: border-box; }
  html, body { width: 668px; height: 1200px; overflow: hidden; background: var(--page); }
  body { position: relative; font-family: "Exo 2", Arial, sans-serif; }

  .billboard {
    position: absolute;
    left: 24px; top: 400px;
    width: 620px; height: 399px;
    background: radial-gradient(ellipse at 50% 20%, var(--plate) 0%, var(--black) 75%);
    overflow: hidden;
  }

  .machine-photo {
    position: absolute;
    left: 0; right: 0; top: 190px; height: 150px;
    background:
      radial-gradient(ellipse at 92% 30%, #e8e8e8 0%, #8c8c8c 18%, rgba(40,40,40,0) 48%),
      linear-gradient(100deg, #070707 0%, #1c1c1c 35%, #3a3a3a 62%, #232323 100%);
  }

  .brand {
    position: absolute;
    top: 14px; left: 0; right: 0;
    display: flex; flex-direction: column; align-items: center;
  }
  .brand-row { display: flex; align-items: center; gap: 8px; }
  .brand-mark {
    width: 14px; height: 14px; border-radius: 50%;
    background: var(--gold);
  }
  .brand-name {
    font-weight: 800; font-size: 34px; line-height: 1;
    letter-spacing: 2px; color: var(--gold);
  }
  .brand-tag {
    margin-top: 3px;
    font-weight: 700; font-size: 9px; letter-spacing: 1.2px;
    color: var(--gold);
  }

  .headline {
    position: absolute;
    top: 70px; left: 0; right: 0;
    text-align: center;
    font-weight: 900; font-style: italic;
    font-size: 52px; line-height: 48px;
    color: var(--gold);
    background: linear-gradient(180deg, var(--gold-light) 0%, var(--gold) 50%, var(--gold-dark) 100%);
    -webkit-background-clip: text; background-clip: text;
    -webkit-text-fill-color: transparent;
  }

  .machine-list {
    position: absolute;
    top: 170px; left: 0; right: 0;
    text-align: center;
    font-weight: 800; font-size: 15.5px; letter-spacing: 0.6px;
    color: var(--white);
  }

  .track-band {
    position: absolute;
    left: 0; right: 0; top: 330px; height: 26px;
    background: linear-gradient(180deg, var(--gold-light) 0%, var(--gold) 45%, var(--gold-dark) 100%);
  }

  .contact {
    position: absolute;
    left: 0; right: 0; top: 363px;
    display: flex; justify-content: center; align-items: center; gap: 20px;
    font-weight: 800; font-size: 18px; letter-spacing: 0.5px;
    color: var(--white);
  }
  .contact-item { display: flex; align-items: center; gap: 7px; }
  .contact-icon { width: 14px; height: 14px; flex: none; }
</style>
</head>
<body>
  <main class="billboard">
    <div class="machine-photo" role="img" aria-label="Black and white night photo of a compact excavator digging with its work lights on"></div>

    <header class="brand">
      <div class="brand-row">
        <span class="brand-mark"></span>
        <span class="brand-name">TALWERK</span>
      </div>
      <span class="brand-tag">BAUMASCHINENVERMIETUNG</span>
    </header>

    <h1 class="headline">THE MACHINES<br>I RENT OUT</h1>

    <p class="machine-list">BAGGER BIS 10T, RADLADER, DUMPER, RAUPENKIPPER</p>

    <div class="track-band" role="img" aria-label="Gold tyre track band"></div>

    <footer class="contact">
      <span class="contact-item">
        <svg class="contact-icon" viewBox="0 0 24 24" fill="none" stroke="#d6ad3c" stroke-width="2" stroke-linecap="round" stroke-linejoin="round">
          <path d="M22 16.9v3a2 2 0 0 1-2.2 2 19.8 19.8 0 0 1-8.6-3.1 19.5 19.5 0 0 1-6-6A19.8 19.8 0 0 1 2.1 4.2 2 2 0 0 1 4.1 2h3a2 2 0 0 1 2 1.7c.1.9.4 1.8.7 2.7a2 2 0 0 1-.5 2.1L8 9.8a16 16 0 0 0 6 6l1.3-1.3a2 2 0 0 1 2.1-.4c.9.3 1.8.6 2.7.7a2 2 0 0 1 1.7 2z"/>
        </svg>
        078 / 513 90 41
      </span>
      <span class="contact-item">
        <svg class="contact-icon" viewBox="0 0 24 24" fill="none" stroke="#d6ad3c" stroke-width="2">
          <circle cx="12" cy="12" r="10"/>
          <path d="M2 12h20M12 2a15 15 0 0 1 0 20M12 2a15 15 0 0 0 0 20"/>
        </svg>
        www.kiesgrube-talwerk.ch
      </span>
    </footer>
  </main>
</body>
</html>
```